Brightfold Systems - IT Service and Consulting
Business Card, Letterhead, Envelopes, Fax templates, and CD Label
Brightfold Systems - IT Service and Consulting -
Creative Brief
Professional
Mara Pellin
Owner
517 W. Orchard Gate Ave #216 Orchard Gate, CA 90482
MPellin@BrightfoldSystems.Com
www.brightfoldsystems.com
We want to communicate that Brightfold Systems is a professional IT Service and Consulting Firm. We want a stationary that conveys professionalism and confidence, at the same time we want to appear unique and approachable to small businesses.
Back should be used to convey the company logo, tagline, and URL.

```html
<!DOCTYPE html>
<html lang="en">
<head>
<meta charset="UTF-8">
<title>Brightfold Systems – Business Card</title>
<link href="https://fonts.googleapis.com/css2?family=Montserrat:wght@400;500;600;700&display=swap" rel="stylesheet">
<style>
  :root {
    --page-bg: #e4e6ea;
    --brand-blue: #1b5fc1;
    --brand-blue-dark: #0f4497;
    --brand-blue-light: #3a7ad6;
    --card-white: #ffffff;
    --card-grey: #eceff3;
    --text-dark: #3a3d42;
    --text-mid: #5d6168;
    --divider: #c4c8ce;
  }
  * { box-sizing: border-box; margin: 0; padding: 0; }
  html, body {
    width: 1200px; height: 901px; overflow: hidden;
    background: var(--page-bg);
    font-family: "Montserrat", Arial, sans-serif;
  }
  .sheet { position: relative; width: 1200px; height: 901px; }

  .card {
    position: absolute; left: 280px; width: 640px; height: 366px;
    border-radius: 4px; overflow: hidden;
    box-shadow: 0 10px 28px rgba(0,0,0,.18);
  }

  /* Back */
  .card-back {
    top: 56px;
    background: linear-gradient(135deg, var(--brand-blue-light) 0%, var(--brand-blue) 45%, var(--brand-blue-dark) 100%);
    color: var(--card-white);
  }
  .card-back .faint-circle {
    position: absolute; left: -70px; top: 120px;
    width: 300px; height: 300px; border-radius: 50%;
    background: rgba(255,255,255,.08);
  }
  .card-back .back-lockup {
    position: absolute; right: 56px; top: 118px; text-align: right;
  }
  .card-back .company-name {
    font-weight: 700; font-size: 42px; letter-spacing: -.5px; line-height: 1;
    color: var(--card-white);
  }
  .card-back .tagline {
    margin-top: 18px; font-size: 12px; font-weight: 500; letter-spacing: 4px;
  }
  .card-back .url {
    margin-top: 10px; font-size: 11px; letter-spacing: 1.5px; opacity: .9;
  }

  /* Front */
  .card-front {
    top: 478px;
    background: linear-gradient(160deg, var(--card-white) 0%, var(--card-white) 45%, var(--card-grey) 100%);
    color: var(--text-dark);
  }
  .front-lockup {
    position: absolute; left: 46px; top: 40px;
    display: flex; align-items: center; gap: 16px;
  }
  .front-lockup .mark {
    width: 62px; height: 62px; border-radius: 50%; background: var(--brand-blue);
  }
  .front-lockup .company-name {
    font-weight: 700; font-size: 36px; letter-spacing: -.5px; line-height: 1;
    color: var(--brand-blue);
  }
  .front-lockup .tagline {
    margin-top: 8px; font-size: 10px; font-weight: 500; letter-spacing: 3.4px;
    color: var(--text-mid);
  }
  .person {
    position: absolute; left: 0; right: 0; top: 168px; text-align: center;
    font-size: 16px;
  }
  .person .name { font-weight: 600; color: var(--brand-blue); }
  .person .sep { color: var(--text-mid); margin: 0 8px; }
  .person .role { color: var(--text-mid); font-size: 14px; }

  .address {
    position: absolute; right: 340px; top: 222px; text-align: right;
    font-size: 13px; line-height: 1.55; color: var(--text-dark);
  }
  .contact-divider {
    position: absolute; left: 316px; top: 218px; width: 1px; height: 52px;
    background: var(--divider);
  }
  .contacts {
    position: absolute; left: 332px; top: 220px;
    font-size: 12.5px; line-height: 1.7; color: var(--text-dark);
  }
  .contacts .row { display: flex; align-items: center; gap: 8px; }
  .contacts svg { width: 13px; height: 13px; fill: var(--text-mid); }
  .corner-mark {
    position: absolute; right: 54px; bottom: 40px;
    width: 36px; height: 36px; border-radius: 50%; background: var(--brand-blue);
  }
  .base-band {
    position: absolute; left: 0; right: 0; bottom: 0; height: 18px;
    background: var(--brand-blue);
    border-top: 4px solid var(--brand-blue-light);
  }
</style>
</head>
<body>
<main class="sheet">

  <section class="card card-back" aria-label="Business card back">
    <div class="faint-circle"></div>
    <div class="back-lockup">
      <div class="company-name">Brightfold Systems</div>
      <div class="tagline">IT MADE CLEAR AND CALM</div>
      <div class="url">www.brightfoldsystems.com</div>
    </div>
  </section>

  <section class="card card-front" aria-label="Business card front">
    <div class="front-lockup">
      <div class="mark"></div>
      <div>
        <div class="company-name">Brightfold Systems</div>
        <div class="tagline">IT MADE CLEAR AND CALM</div>
      </div>
    </div>

    <div class="person">
      <span class="name">Mara Pellin</span><span class="sep">/</span><span class="role">Owner</span>
    </div>

    <div class="address">
      517 W. Orchard Gate Ave #216<br>
      Orchard Gate, CA 90482
    </div>
    <div class="contact-divider"></div>
    <div class="contacts">
      <div class="row">
        <svg viewBox="0 0 24 24" aria-hidden="true"><path d="M6.6 10.8a15.1 15.1 0 0 0 6.6 6.6l2.2-2.2c.3-.3.7-.4 1-.2 1.1.4 2.3.6 3.6.6.6 0 1 .4 1 1V20c0 .6-.4 1-1 1A17 17 0 0 1 3 4c0-.6.4-1 1-1h3.5c.6 0 1 .4 1 1 0 1.3.2 2.5.6 3.6.1.3 0 .7-.2 1z"/></svg>
        <span>555-014-2290</span>
      </div>
      <div class="row">
        <svg viewBox="0 0 24 24" aria-hidden="true"><path d="M3 5h18v14H3zm2 2v.5l7 4.5 7-4.5V7zm0 2.9V17h14V9.9l-7 4.5z"/></svg>
        <span>MPellin@BrightfoldSystems.Com</span>
      </div>
    </div>

    <div class="corner-mark"></div>
    <div class="base-band"></div>
  </section>

</main>
</body>
</html>
```